Graphic lion print design with text

I like the gold effects in image 2 as described in my attached document, but i'm open to other suggestions. The desired image is image 1. This is a gift for a Leo friend. This is going to be printed and framed to be hung on the wall in a large frame, in landscape format. I like the idea of using different font styles to separate the statements.

• I’m open to the suggestions about the font styles, but I want to separate the statements by using different font styles as shown in attached document.
Must be landscape format.
Small fonts preferred, as shown in the attached image.
• I like the gold effect in image 2 but other suggestions/colours welcome
• Please don't stretch the picture so I can have a good resolution. Place the text on another black background template and then paste the picture beside to the text.

```html
<!DOCTYPE html>
<html lang="en">
<head>
<meta charset="utf-8">
<title>Lion Print – For God Is With You</title>
<link rel="stylesheet" href="https://fonts.googleapis.com/css2?family=UnifrakturMaguntia&family=Rochester&family=Quicksand:wght@700&family=Pacifico&family=Lobster&family=Open+Sans:wght@400&family=Cormorant+Garamond:wght@500&family=Comic+Neue:wght@400&family=Abril+Fatface&family=Archivo+Narrow:wght@700&display=swap">
<style>
  :root {
    --black: #000000;
    --gold: #c9a84b;
    --gold-light: #e9d27a;
    --gold-deep: #8c5e2c;
    --gold-bright: #f5e47e;
    --gold-muted: #a8833a;
    --ink: #0b0905;
  }
  * { margin: 0; padding: 0; box-sizing: border-box; }
  html, body {
    width: 1200px; height: 732px; overflow: hidden; background: var(--black);
  }
  .poster {
    position: relative; width: 1200px; height: 732px; background: var(--black); overflow: hidden;
  }

  /* Lion artwork area */
  .lion-art {
    position: absolute; left: 740px; top: 0; width: 460px; height: 690px;
    background:
      radial-gradient(ellipse 60% 55% at 62% 48%, #e3c66b 0%, #b88d3c 35%, #6d4a1e 65%, rgba(0,0,0,0) 100%);
    z-index: 1;
  }

  /* Top gold band */
  .banner {
    position: absolute; left: 0; top: 15px; width: 850px; height: 103px;
    background: linear-gradient(90deg, #b8833f 0%, var(--gold-deep) 17%, var(--gold-muted) 34%, var(--gold-bright) 54%, #cdb052 72%, #7a5f23 90%, var(--black) 100%);
    z-index: 2;
    color: var(--ink);
  }
  .banner__headline {
    position: absolute; left: 26px; top: 8px;
    font-family: "UnifrakturMaguntia", serif; font-size: 29px; white-space: nowrap;
  }
  .banner__tagline {
    position: absolute; left: 275px; top: 49px;
    font-family: "Archivo Narrow", sans-serif; font-weight: 700; font-size: 23px;
    letter-spacing: -1.6px; white-space: nowrap;
  }
  .banner__subline {
    position: absolute; left: 177px; top: 79px;
    font-family: "Open Sans", sans-serif; font-size: 17px; letter-spacing: 2px; white-space: nowrap;
  }

  /* Left framed panel */
  .blessing {
    position: absolute; left: 33px; top: 138px; width: 298px; height: 584px;
    border: 3px solid var(--gold-muted);
    color: var(--gold);
    z-index: 2;
  }
  .blessing > * { position: absolute; left: 17px; white-space: nowrap; line-height: 1; }
  .blessing__script { font-family: "Rochester", cursive; font-size: 38px; color: var(--gold-light); }
  .blessing__bold { font-family: "Quicksand", sans-serif; font-weight: 700; font-size: 32px; color: var(--gold-light); }
  .blessing__brush { font-family: "Pacifico", cursive; font-size: 23px; color: var(--gold-light); }
  .blessing__him { font-family: "Lobster", cursive; font-size: 36px; color: var(--gold-light); }
  .blessing__plain { font-family: "Open Sans", sans-serif; font-size: 21px; }
  .blessing__serif { font-family: "Cormorant Garamond", serif; font-weight: 500; font-size: 20px; transform: scaleX(0.85); transform-origin: left; }
  .blessing__casual { font-family: "Comic Neue", cursive; font-size: 22px; color: var(--gold-light); letter-spacing: 1px; line-height: 1.05; }
  .blessing__doors { font-family: "Abril Fatface", serif; font-size: 21px; color: var(--gold-light); }
  .blessing__small { font-family: "Open Sans", sans-serif; font-size: 18px; }
  .blessing__gothic { font-family: "UnifrakturMaguntia", serif; font-size: 22px; color: var(--gold-light); }

  /* Bottom promise */
  .promise {
    position: absolute; left: 340px; top: 634px; width: 585px;
    text-align: center; font-family: "Open Sans", sans-serif; font-size: 22px; line-height: 30px;
    color: var(--gold-muted); z-index: 3;
  }
  .promise__amen { color: var(--gold-light); }
</style>
</head>
<body>
  <main class="poster">
    <div class="lion-art" role="img" aria-label="Gold illustrated roaring lion head in profile with flowing mane, facing left"></div>

    <header class="banner">
      <p class="banner__headline">It doesn’t matter who or what may come against you,</p>
      <p class="banner__tagline">FORGODISWITHYOU</p>
      <p class="banner__subline">HE has made you more than a conqueror.</p>
    </header>

    <section class="blessing">
      <p class="blessing__script" style="top:8px;">Almighty God</p>
      <p class="blessing__bold" style="top:63px;">will come</p>
      <p class="blessing__bold" style="top:98px;">through for you</p>
      <p class="blessing__brush" style="top:134px;">when you seek</p>
      <p class="blessing__him" style="top:177px;">Him</p>
      <p class="blessing__plain" style="left:103px; top:188px;">in your moments</p>
      <p class="blessing__plain" style="top:216px;">of trouble and unrest.</p>

      <p class="blessing__bold" style="top:292px; font-size:33px;">May God</p>
      <p class="blessing__serif" style="top:334px;">calm the restlessness of your mind</p>
      <p class="blessing__script" style="top:358px;">And</p>
      <p class="blessing__casual" style="top:400px;">still the thoughts that<br>worry you.</p>

      <p class="blessing__doors" style="top:492px;">DOORS</p>
      <p class="blessing__small" style="left:100px; top:494px;">will open for</p>
      <p class="blessing__small" style="top:524px;">you, <span class="blessing__gothic">in the most</span></p>
      <p class="blessing__gothic" style="top:553px;">unlikeliest of places.</p>
    </section>

    <p class="promise">
      When you go through deep waters, He will be with you.<br>
      Never will He leave you, Never will He forsake you.<br>
      <span class="promise__amen">Amen.</span>
    </p>
  </main>
</body>
</html>
```